Vitamin/Dietary Supplement Company needs a simple Hemp CBD Health retail website to display a few...

We need a simple website designed that will allow us to display a few products for purchase. We are a vitamin/dietary supplement company that wants to set up a separate website for CBD health products. CBD is a chemical compound found in hemp and cannabis plants that provide various health and medicinal benefits. Our target audience are individuals that suffer from health issues and would like to treat their pain relief with CBD as an alternative to prescription medication and over the counter drugs such as Paxorin and Dolvex. Looking for a simple and clean website that is easy for customers to navigate and purchase products.

Need extra days to review

Target Market(s)

Our target audience are individuals that suffer from health issues and would like to treat their pain relief with CBD as an alternative to prescription medication and over the counter drugs such as Paxorin and Dolvex.

Coding

Coded - Design and coding required

Font styles to use
Serif

Colors

Designer to choose colors to be used in the design.

Requirements
Nice to have
• Homepage, About page, FAQ page, Contact page, Blog page

```html
<!DOCTYPE html>
<html lang="en">
<head>
<meta charset="utf-8">
<title>Verdant Calm – CBD Health Products</title>
<link href="https://fonts.googleapis.com/css2?family=Poppins:wght@300;400;500;600;700&display=swap" rel="stylesheet">
<style>
:root{
  --green:#7b9c3b;
  --green-dark:#5f7f27;
  --ink:#2f2f2f;
  --dark:#3d3d3d;
  --darker:#2b2b2b;
  --white:#fff;
  --card:#e6e6e6;
}
*{box-sizing:border-box;margin:0;padding:0}
html,body{width:1200px;height:3075px;overflow:hidden}
body{font-family:'Poppins',sans-serif;color:var(--ink);background:var(--white);position:relative}
a{color:inherit;text-decoration:none}
.abs{position:absolute}

/* header */
.site-header{position:absolute;left:0;top:0;width:1200px;height:135px;background:var(--white);border-bottom:1px solid #ddd}
.brand{position:absolute;left:101px;top:48px;display:flex;align-items:center;gap:10px}
.brand-dot{width:34px;height:34px;border-radius:50%;background:var(--green)}
.brand-name{font-weight:700;font-size:22px;color:var(--green);letter-spacing:.5px}
.contact-strip{position:absolute;top:24px;display:flex;align-items:center;gap:8px;font-size:13px;line-height:17px}
.contact-strip small{display:block;color:#666;font-size:13px}
.contact-strip b{font-weight:600;font-size:13px;color:var(--ink)}
.main-nav{position:absolute;top:98px;left:404px;display:flex;gap:28px;font-size:16px;color:#333}

/* hero */
.hero{position:absolute;left:0;top:135px;width:1200px;height:537px;
  background:radial-gradient(ellipse at 20% 30%,#7d6fa8 0%,#4a4560 30%,transparent 55%),
  radial-gradient(ellipse at 85% 35%,#d3a84a 0%,transparent 40%),
  radial-gradient(ellipse at 55% 78%,#cdbfa5 0%,#8a7f6c 30%,transparent 55%),
  linear-gradient(180deg,#4a4a45,#2c2a25)}
.hero h1{position:absolute;top:165px;width:100%;text-align:center;color:var(--white);font-size:46px;font-weight:700;letter-spacing:2px}
.hero p{position:absolute;top:233px;left:350px;width:500px;text-align:center;color:var(--white);font-size:18px;line-height:36px;font-weight:500}
.hero-btn{position:absolute;top:322px;height:55px;border:2px solid var(--white);border-radius:28px;color:var(--white);font-weight:600;font-size:18px;display:flex;align-items:center;justify-content:center;gap:8px}
.hero-arrow{position:absolute;top:253px;width:36px;height:36px;border:2px solid var(--white);border-radius:50%}

/* products */
.section-title{position:absolute;width:100%;text-align:center;color:var(--green);font-weight:700;font-size:34px}
.product{position:absolute;width:237px;text-align:center}
.product-photo{height:257px;background:linear-gradient(160deg,#ececec,#d9d9d9);box-shadow:0 2px 4px rgba(0,0,0,.08);position:relative}
.product-photo.hover{background:linear-gradient(160deg,#b9b9b9,#a6a6a6)}
.product-name{margin-top:22px;color:var(--green);font-weight:600;font-size:20px}
.product-price{margin-top:6px;font-size:18px;color:#333}
.card-action{position:absolute;bottom:18px;height:26px;font-size:12px;display:flex;align-items:center;gap:5px;padding:0 8px}
.view-more{position:absolute;left:507px;top:1621px;width:188px;height:54px;border:3px solid var(--green);border-radius:28px;color:var(--green);font-weight:600;font-size:17px;display:flex;align-items:center;justify-content:center;gap:8px}

/* about */
.about{position:absolute;left:0;top:1780px;width:1200px;height:584px;background:linear-gradient(120deg,#7a9b3c,#6f9033 60%,#7c9d3e)}
.about-frame{position:absolute;left:95px;top:122px;width:400px;height:303px;border:4px solid var(--white)}
.about-photo{position:absolute;left:116px;top:141px;width:407px;height:321px;background:linear-gradient(150deg,#f0f0f0,#d6d6d6)}
.about h2{position:absolute;left:563px;top:152px;color:var(--white);font-weight:700;font-size:32px}
.about p{position:absolute;left:563px;top:200px;width:554px;color:var(--white);font-size:16px;line-height:31px;font-weight:300;text-align:justify}
.about-btn{position:absolute;left:563px;top:400px;width:143px;height:44px;border:2px solid var(--white);border-radius:24px;color:var(--white);font-weight:600;font-size:16px;display:flex;align-items:center;justify-content:center}

/* dark footer */
.footer{position:absolute;left:0;top:2364px;width:1200px;height:665px;background:var(--dark);color:var(--white)}
.feature{position:absolute;top:58px;width:282px;height:184px;border:2px solid var(--green);background:#454545;text-align:center;padding-top:36px}
.feature h3{font-weight:500;font-size:19px;margin-top:12px}
.feature p{font-size:16px;margin-top:6px;font-weight:500}
.footer-col{position:absolute;top:330px}
.footer-col h4{color:var(--green);font-weight:700;font-size:22px;margin-bottom:22px}
.footer-col li{list-style:none;font-size:16px;line-height:30px;font-weight:300}
.footer-col .about-text{font-size:13px;line-height:23px;width:245px;font-weight:300}
.social{display:flex;gap:10px;margin-top:26px}
.social span{width:30px;height:30px;border-radius:50%;background:var(--green)}
.subscribe{display:flex;width:313px;height:44px;border:1px solid #bbb;margin-top:20px;padding:2px}
.subscribe input{flex:1;background:transparent;border:0;color:#ddd;font-family:inherit;font-size:10px;padding-left:8px}
.subscribe button{width:92px;background:var(--green);border:0;color:var(--white);font-family:inherit;font-size:12px;font-weight:500}
.bottom-bar{position:absolute;left:0;top:3029px;width:1200px;height:46px;background:var(--darker);color:var(--white)}
.bottom-bar p{position:absolute;left:97px;top:14px;font-size:13px}
.pay{position:absolute;top:15px;width:29px;height:19px;border-radius:2px}
</style>
</head>
<body>

<header class="site-header">
  <div class="brand"><span class="brand-dot"></span><span class="brand-name">VERDANT CALM</span></div>

  <div class="contact-strip" style="left:462px">
    <svg width="34" height="34" viewBox="0 0 34 34"><circle cx="17" cy="17" r="17" fill="#7b9c3b"/><path d="M11 9c2 0 3 4 2 5l-1 1c1 3 3 5 6 6l1-1c1-1 5 0 5 2 0 2-2 3-4 3-7-1-12-6-12-12 0-2 1-4 3-4z" fill="#fff"/></svg>
    <div><small>Call us on:</small><b>888888888</b></div>
  </div>
  <div class="contact-strip" style="left:623px">
    <svg width="44" height="30" viewBox="0 0 44 30"><rect x="1" y="1" width="42" height="28" fill="#7b9c3b"/><path d="M1 1l21 17L43 1M1 29l16-14M43 29L27 15" stroke="#fff" stroke-width="2" fill="none"/></svg>
    <div><small>Mail us on:</small><b>INFO@VERDANTCALM.COM</b></div>
  </div>
  <div class="contact-strip" style="left:870px">
    <svg width="36" height="32" viewBox="0 0 36 32"><path d="M18 31C6 21 1 16 1 9 1 4 5 1 10 1c4 0 6 2 8 5 2-3 4-5 8-5 5 0 9 3 9 8 0 7-5 12-17 22z" fill="#7b9c3b"/></svg>
    <div><small>0 Items</small><b>WISHLIST</b></div>
  </div>
  <div class="contact-strip" style="left:1007px">
    <svg width="40" height="36" viewBox="0 0 40 36"><path d="M2 3h6l5 20h20l4-14H11" stroke="#7b9c3b" stroke-width="3" fill="none"/><circle cx="15" cy="31" r="3" fill="#7b9c3b"/><circle cx="31" cy="31" r="3" fill="#7b9c3b"/></svg>
    <div><small>0 Items</small><b>CART</b></div>
  </div>

  <nav class="main-nav">
    <a href="#">Home</a><a href="#">Shop For Cbd Oil</a><a href="#">Cbd Oil FAQ's</a><a href="#">Contact Us</a><a href="#">Cbd News Blog</a><a href="#">About Us</a>
  </nav>
</header>

<section class="hero" role="img" aria-label="Photo of CBD capsules on a wooden surface with purple lavender flowers and a bottle of oil">
  <svg class="hero-arrow" style="left:32px" viewBox="0 0 36 36"><path d="M20 10l-8 8 8 8" stroke="#fff" stroke-width="2.5" fill="none"/></svg>
  <svg class="hero-arrow" style="left:1131px" viewBox="0 0 36 36"><path d="M15 10l8 8-8 8" stroke="#fff" stroke-width="2.5" fill="none"/></svg>
  <h1>WELCOME TO VERDANT CALM</h1>
  <p>Sed ut perspiciatis unde omnis iste natus error sit voluptatem accusantium doloremque</p>
  <a class="hero-btn" href="#" style="left:409px;width:181px">
    <svg width="22" height="16" viewBox="0 0 22 16"><path d="M1 2h4l3 10h10l2-7H7" stroke="#fff" stroke-width="1.8" fill="none" stroke-dasharray="3 2"/></svg>Shop Now</a>
  <a class="hero-btn" href="#" style="left:603px;width:188px">
    <svg width="18" height="18" viewBox="0 0 18 18"><path d="M17 1L1 8l7 2 2 7z" fill="#fff"/></svg>Contact us</a>
</section>

<h2 class="section-title" style="top:766px">OUR PRODUCTS</h2>
<svg class="abs" style="left:463px;top:812px" width="274" height="26" viewBox="0 0 274 26">
  <line x1="0" y1="15" x2="108" y2="15" stroke="#7b9c3b" stroke-width="2"/>
  <line x1="166" y1="15" x2="274" y2="15" stroke="#7b9c3b" stroke-width="2"/>
  <path d="M137 2l4 8 8 1-6 5 2 8-8-4-8 4 2-8-6-5 8-1z" fill="#7b9c3b"/>
  <path d="M120 12l2 4h4l-3 3 1 4-4-2-4 2 1-4-3-3h4zM154 12l2 4h4l-3 3 1 4-4-2-4 2 1-4-3-3h4z" fill="#7b9c3b"/>
</svg>

<div class="product" style="left:100px;top:869px"><div class="product-photo" role="img" aria-label="Product photo of brown and green CBD tincture jars"></div><div class="product-name">PRODUCT NAME</div><div class="product-price">$29.00</div></div>
<div class="product" style="left:355px;top:869px"><div class="product-photo" role="img" aria-label="Product photo of a jar of yellow cannabis infused candies"></div><div class="product-name">PRODUCT NAME</div><div class="product-price">$19.00</div></div>
<div class="product" style="left:609px;top:869px"><div class="product-photo hover" role="img" aria-label="Product photo of a jar of red cannabis infused candies">
  <span class="card-action" style="left:14px;background:var(--green);color:#fff"><svg width="12" height="11" viewBox="0 0 36 32"><path d="M18 31C6 21 1 16 1 9 1 4 5 1 10 1c4 0 6 2 8 5 2-3 4-5 8-5 5 0 9 3 9 8 0 7-5 12-17 22z" fill="#fff"/></svg>Wish List</span>
  <span class="card-action" style="left:118px;background:#fff;color:#333"><svg width="14" height="11" viewBox="0 0 22 16"><path d="M1 2h4l3 10h10l2-7H7" stroke="#333" stroke-width="1.8" fill="none"/></svg>Add to cart</span>
</div><div class="product-name">PRODUCT NAME</div><div class="product-price">$99.00</div></div>
<div class="product" style="left:863px;top:869px"><div class="product-photo" role="img" aria-label="Product photo of a green edibles pouch with colourful containers"></div><div class="product-name">PRODUCT NAME</div><div class="product-price">$59.00</div></div>

<div class="product" style="left:100px;top:1245px"><div class="product-photo" role="img" aria-label="Product photo of brown and green CBD tincture jars"></div><div class="product-name">PRODUCT NAME</div><div class="product-price">$29.00</div></div>
<div class="product" style="left:355px;top:1245px"><div class="product-photo" role="img" aria-label="Product photo of a jar of yellow cannabis infused candies"></div><div class="product-name">PRODUCT NAME</div><div class="product-price">$19.00</div></div>
<div class="product" style="left:609px;top:1245px"><div class="product-photo" role="img" aria-label="Product photo of a jar of red cannabis infused candies"></div><div class="product-name">PRODUCT NAME</div><div class="product-price">$99.00</div></div>
<div class="product" style="left:863px;top:1245px"><div class="product-photo" role="img" aria-label="Product photo of a green edibles pouch with colourful containers"></div><div class="product-name">PRODUCT NAME</div><div class="product-price">$59.00</div></div>

<a class="view-more" href="#"><svg width="16" height="16" viewBox="0 0 16 16"><path d="M13 6A5.5 5.5 0 0 0 3 5M3 10a5.5 5.5 0 0 0 10 1" stroke="#7b9c3b" stroke-width="2" fill="none"/><path d="M14 1v5h-5M2 15v-5h5" stroke="#7b9c3b" stroke-width="2" fill="none"/></svg>View More</a>

<section class="about">
  <div class="about-frame"></div>
  <div class="about-photo" role="img" aria-label="Photo of CBD pouches, a vape pen and colourful containers on a white table"></div>
  <h2>ABOUT US</h2>
  <p>Sed ut perspiciatis unde omnis iste natus error sit voluptatem accusantium doloremque laudantium, totam rem aperiam, eaque ipsa quae ab illo inventore veritatis et quasi architecto beatae vitae dicta sunt explicabo. Nemo enim ipsam voluptatem quia voluptas sit aspernatur aut odit aut fugit, sed quia consequuntur magni dolores eos qui ratione voluptatem sequi nesciunt.</p>
  <a class="about-btn" href="#">Read more</a>
</section>

<footer class="footer">
  <div class="feature" style="left:113px">
    <svg width="46" height="40" viewBox="0 0 46 40"><path d="M4 10h36v26H4zM8 10l20-8 4 8" stroke="#fff" stroke-width="2" fill="none"/><rect x="28" y="18" width="14" height="10" stroke="#fff" stroke-width="2" fill="none"/><circle cx="34" cy="23" r="2" fill="#fff"/></svg>
    <h3>Terms of Payment</h3><p>Sed ut perspiciatis unde</p>
  </div>
  <div class="feature" style="left:460px">
    <svg width="36" height="44" viewBox="0 0 36 44"><rect x="3" y="2" width="30" height="34" rx="5" stroke="#fff" stroke-width="2" fill="none"/><path d="M8 8h20v14H8zM3 26h30" stroke="#fff" stroke-width="2" fill="none"/><circle cx="10" cy="31" r="2" fill="#fff"/><circle cx="26" cy="31" r="2" fill="#fff"/><path d="M8 36v6M28 36v6" stroke="#fff" stroke-width="2"/></svg>
    <h3>Quick Delivery</h3><p>Sed ut perspiciatis unde omnis</p>
  </div>
  <div class="feature" style="left:805px">
    <svg width="46" height="40" viewBox="0 0 46 40"><circle cx="18" cy="12" r="7" stroke="#fff" stroke-width="2" fill="none"/><path d="M3 36c0-9 7-14 15-14s15 5 15 14z" stroke="#fff" stroke-width="2" fill="none"/><circle cx="32" cy="9" r="6" stroke="#fff" stroke-width="2" fill="none"/><path d="M33 19c6 0 11 4 11 12h-8" stroke="#fff" stroke-width="2" fill="none"/></svg>
    <h3 style="font-size:18px">Support: 88888888</h3><p>email: info@verdantcalm</p>
  </div>

  <div class="footer-col" style="left:99px">
    <h4>VERDANT CALM</h4>
    <p class="about-text">Duis aute irure dolor in reprehendrit in voluptate velit esse cillum dolore eu fugiat nulla pariatur.</p>
    <div class="social"><span></span><span></span><span></span><span></span></div>
    <form class="subscribe"><input type="text" placeholder="Enter your e-mail"><button type="button">SUBSCRIBE</button></form>
  </div>
  <div class="footer-col" style="left:454px">
    <h4>INFORMATIONS</h4>
    <ul><li>About us</li><li>Delivery information</li><li>Terms of Business</li></ul>
  </div>
  <div class="footer-col" style="left:672px">
    <h4>QUICK LINKS</h4>
    <ul><li>Shop For Cbd Products</li><li>Cbd Products FAQ's</li><li>Contact Us</li><li>Cbd News Blog</li><li>About Us</li></ul>
  </div>
  <div class="footer-col" style="left:890px">
    <h4>CUSTOMER SERVICE</h4>
    <ul><li>Contact</li><li>Site map</li><li>Gift certificates</li></ul>
  </div>
</footer>

<div class="bottom-bar">
  <p>Copyrights © 2018 - All Rights are Reserved</p>
  <span class="pay" style="left:524px;background:#e8e8e8"></span>
  <span class="pay" style="left:565px;background:#3a5bb0"></span>
  <span class="pay" style="left:606px;background:#e8e8e8"></span>
  <span class="pay" style="left:647px;background:#2a6fc9"></span>
</div>

</body>
</html>
```